Doctor Formulated Medical Cosmetics

Orvan Kesto is an E-commerce site for high end Medical Cosmetics designed to treat specific skin problems. The Orvan Kesto difference/advantage is that all creams and serums are:
Doctor Formulated, Freshly Handmade, Registered Pharmacy.
The Site also provides real doctor Dermatology Consultations, Library (with a list of - 1. Active Ingredients in the creams with description of their effects, 2. Skin Conditions with information on what causes the condition and typical treatment approaches and outcomes. 3. Resources from Dermatology Journals and literature on the conditions.)
Header Information: Orvan Kesto, languages EN, BG, Register / log in, Shopping Bag. This field should be narrow.
Categories (horizontal): Home, Face, Body, Hair Care, Skin Conditions, Doctor Consultation, Library
The Landing Page should have only one well organized picture, which is intended to create the feeling of luxury, freedom and relaxation. It will be large and will fill the whole screen. All text should be on transparent or similar color fields. Please use the color of the text to create also the feeling of conservative luxury.
Written message / image overlay Orvan Kesto(logo), Skin Care, Doctor Formulated, Freshly Handmade, Registered Pharmacy.
Please study the Landing Page of this site as an example: www.tamerivo.com
Under the Landing Page, there should be a slider with 4 of our products.
Underneath: Four Blog Articles (large pictures for maximum impact and luxury text underneath).
Underneath: Banner for Dermatologist Consultation, (button for Start Your Case Now).
Underneath: Two pictures in a line - Library (with books), and Active Ingredients.
Footer: Philosophy, Categories, Customer Care
Please adhere to the color palate provided in the pictures (as attachments). Provided are some examples of Web Sites with the desired look and feel. www.brulin.com , www.halvestinemd.com .
Please use different shades of gray, white, beige and gold colors, and black. Our products will be in brown glass jars and bottles to convey the professional, pharmacy made nature of the creams and lotions.
We find the following Front Page very attractive and effective - www.tamerivo.com , with its full page image and overlaying text.
Please have a look at this link for the Landing page.
http://www.plovatrex.com/detail/video/woman-lying-on-a-black-sand-beach-in-a-bikini-stock-footage/31862057
I would like to use it in the animated version to achieve the WOW effect. I have uploaded the jpeg version for it, so you will be able create your design.
For the Landing page design, please use only the two uploaded pictures of a woman laying at the beach. Let's see how each of them will look like.
Thank you for your help.
Club
1 page

```html
<!DOCTYPE html>
<html lang="en">
<head>
<meta charset="utf-8">
<title>Orvan Kesto — Doctor Formulated Medical Cosmetics</title>
<link href="https://fonts.googleapis.com/css2?family=Lato:wght@300;400;700&family=Pinyon+Script&display=swap" rel="stylesheet">
<style>
:root{
  --header:#a9a6a3;
  --header-dark:#8f8c89;
  --nav-text:#f4f1ee;
  --accent:#c9895b;
  --accent-soft:#e0b38f;
  --ink:#4a4440;
  --muted:#8d8682;
  --line:#ddd6d0;
  --paper:#ffffff;
  --panel:#5c4d42;
  --consult:#2d2a28;
  --beige:#fbe6cc;
  --footer:#1f1c1b;
  --footer-text:#bfb7b1;
}
*{box-sizing:border-box;margin:0;padding:0}
html,body{width:1200px;height:3012px;overflow:hidden}
body{font-family:"Lato",sans-serif;color:var(--ink);background:var(--paper);position:relative}
a{color:inherit;text-decoration:none}

/* Header */
.site-header{position:absolute;top:0;left:0;width:1200px;height:148px;background:var(--header)}
.brand{position:absolute;left:44px;top:20px;display:flex;align-items:center;gap:14px}
.brand-mark{width:60px;height:60px;background:var(--nav-text)}
.brand-name{font-size:30px;font-weight:300;color:var(--nav-text);letter-spacing:1px}
.utility{position:absolute;right:60px;top:56px;display:flex;gap:22px;font-size:12px;letter-spacing:1px;color:var(--nav-text);align-items:center}
.utility .lang{border:1px solid var(--nav-text);padding:2px 6px}
.utility svg{width:22px;height:22px}
.main-nav{position:absolute;left:0;right:0;top:104px;display:flex;justify-content:center;gap:58px;font-size:13px;letter-spacing:1.5px;color:var(--nav-text);text-transform:uppercase}

/* Hero */
.hero{position:absolute;top:148px;left:0;width:1200px;height:432px;background:linear-gradient(90deg,#e8d6c8 0%,#efe6df 35%,#dcd9d6 60%,#cfcbc7 100%)}
.hero-photo{position:absolute;left:0;top:0;width:460px;height:432px;background:radial-gradient(ellipse at 45% 50%,#e9c3a7 0%,#dcb79c 40%,#e8ddd4 85%)}
.hero-card{position:absolute;left:452px;top:92px;width:580px;height:232px;background:rgba(255,255,255,.85);text-align:center;padding:26px 40px}
.hero-card h1{font-family:"Pinyon Script",cursive;font-weight:400;font-size:48px;color:var(--ink)}
.hero-card .lead{font-size:20px;margin-top:10px;color:var(--ink)}
.hero-card .copy{font-size:14px;line-height:20px;margin-top:14px;color:var(--muted)}
.dots{position:absolute;left:584px;top:392px;display:flex;gap:10px}
.dots span{width:9px;height:9px;border-radius:50%;background:#fff}
.dots span.on{background:var(--ink)}

/* Best sellers */
.best{position:absolute;top:660px;left:0;width:1200px;text-align:center}
.section-script{display:flex;align-items:center;justify-content:center;gap:20px;font-size:32px;font-weight:300;color:var(--accent)}
.section-script::before,.section-script::after{content:"";width:210px;height:1px;background:var(--accent-soft)}
.best .intro{width:600px;margin:20px auto 0;font-size:13px;line-height:20px;color:var(--muted)}
.best .intro b{color:var(--ink)}
.products{position:absolute;top:180px;left:172px;width:860px;display:flex;justify-content:space-between}
.product{width:180px;text-align:center}
.product-shot{height:220px;margin:0 auto;width:150px}
.product h3{margin-top:36px;font-size:14px;font-weight:700;color:var(--accent)}
.product p{font-size:12px;line-height:16px;color:var(--muted);margin-top:6px}
.product .price{font-size:17px;font-weight:700;color:var(--ink);margin-top:16px}
.btn-outline{display:inline-block;border:1px solid var(--accent-soft);border-radius:18px;padding:8px 22px;font-size:12px;letter-spacing:1px;color:var(--ink);margin-top:18px}
.arrow{position:absolute;top:390px;width:30px;height:30px}

.rule{position:absolute;left:0;width:1200px;height:1px;background:var(--line)}

/* Blog */
.blog-title{position:absolute;top:1402px;left:172px;font-size:30px;font-weight:300;color:var(--muted);letter-spacing:1px}
.blog-title-rule{position:absolute;top:1458px;left:172px;width:860px;height:1px;background:var(--line)}
.post{position:absolute;top:1506px;width:420px}
.post-photo{height:222px}
.post-panel{background:var(--panel);height:192px;padding:34px 24px;color:#f1e9e3}
.post-panel h3{font-weight:300;font-size:28px;line-height:34px}
.post-panel p{font-size:15px;margin-top:14px;color:#d6cbc2}
.post .btn-outline{position:absolute;top:428px;left:176px;padding:4px 16px;font-size:10px;margin:0}

/* Consultation */
.consult{position:absolute;top:2020px;left:0;width:1200px;height:480px;background:radial-gradient(ellipse at 50% 50%,#4a4542 0%,var(--consult) 70%);text-align:center;color:#f1ece8}
.consult h2{font-weight:400;font-size:30px;margin-top:58px}
.consult .copy{width:620px;margin:14px auto 0;font-size:13px;line-height:20px;color:#c9c1bb}
.doctor{width:144px;height:144px;border-radius:50%;border:5px solid #fff;margin:40px auto 0;background:radial-gradient(circle at 50% 40%,#e6e1dc,#b8b2ad)}
.consult .quote{font-size:20px;font-weight:300;margin-top:32px}
.consult-nav{display:flex;justify-content:center;gap:8px;margin-top:20px}
.consult-nav span{width:22px;height:22px;border:1px solid #cfc7c1;border-radius:50%;font-size:12px;line-height:20px}

/* Newsletter */
.signup{position:absolute;top:2520px;left:0;width:1200px;height:100px;background:var(--beige)}
.signup h4{position:absolute;top:20px;font-size:14px;font-weight:700;color:var(--ink)}
.signup-form{position:absolute;left:172px;top:52px;display:flex}
.signup-form .field{width:270px;height:28px;background:#fff;border:1px solid var(--line);font-size:11px;color:var(--muted);padding:6px 10px}
.signup-form .submit{height:28px;background:var(--accent);color:#fff;font-size:12px;font-weight:700;padding:7px 16px;margin-left:8px;letter-spacing:1px}
.social{position:absolute;left:760px;top:50px;display:flex;gap:14px}
.social span{width:28px;height:28px;border-radius:50%;background:var(--accent)}

/* Footer */
.site-footer{position:absolute;top:2620px;left:0;width:1200px;height:392px;background:var(--footer);color:var(--footer-text)}
.footer-col{position:absolute;top:46px;width:260px}
.footer-col h5{font-size:15px;font-weight:700;color:#fff;margin-bottom:20px}
.footer-col li{list-style:none;font-size:12px;line-height:23px}
.copyright{position:absolute;bottom:20px;width:100%;text-align:center;font-size:10px;color:#7d7672}
</style>
</head>
<body>

<header class="site-header">
  <div class="brand"><span class="brand-mark"></span><span class="brand-name">Orvan Kesto</span></div>
  <div class="utility">
    <span>REGISTER</span><span>|</span><span>MY BAG</span><span>|</span><span>LOG IN</span><span class="lang">EN</span><span class="lang">BG</span>
    <svg viewBox="0 0 24 24" fill="none" stroke="#f4f1ee" stroke-width="2"><circle cx="10" cy="10" r="6"/><line x1="15" y1="15" x2="21" y2="21"/></svg>
  </div>
  <nav class="main-nav"><a>Face</a><a>Body</a><a>Hair Care</a><a>Skin Concerns</a><a>Dermatologist</a><a>Consultation</a><a>Library</a></nav>
</header>

<section class="hero">
  <div class="hero-photo" role="img" aria-label="Portrait of a woman with glowing skin"></div>
  <div class="hero-card">
    <h1>Freshly Handmade</h1>
    <p class="lead">Nullam suscipit pretium lacus, eu aliquet nunc egestas vitae</p>
    <p class="copy">Duis luctus, nunc ut tincidunt elementum, tellus enim rutrum sapien, ultrices sollicitudin lorem nisl non diam. Quisque ac velit massa, ac dapibus ipsum tristique vel, elementum nisi.</p>
  </div>
  <div class="dots"><span class="on"></span><span></span><span></span></div>
</section>

<section class="best">
  <h2 class="section-script">Shop Best Sellers</h2>
  <p class="intro">Donec rhoncus vitae nunc sed elementum <b>integer tincidunt, sapien vitae convallis hendrerit, diam velit sagittis justo,</b> tristique sodales neque nunc sit amet ex.</p>
  <svg class="arrow" style="left:100px" viewBox="0 0 30 30" fill="none" stroke="#4a4440" stroke-width="3"><polyline points="19,7 11,15 19,23"/></svg>
  <svg class="arrow" style="right:100px" viewBox="0 0 30 30" fill="none" stroke="#4a4440" stroke-width="3"><polyline points="11,7 19,15 11,23"/></svg>
  <div class="products">
    <div class="product">
      <div class="product-shot" role="img" aria-label="Brown glass serum bottles" style="background:linear-gradient(180deg,#f7f3ef,#8a5a2e 60%,#5e3a1c)"></div>
      <h3>Vestibulum Purus</h3><p>Condimentum ultricies ut ipsum Quam auctor euismod</p><div class="price">$142.00</div><a class="btn-outline">ADD TO CART</a>
    </div>
    <div class="product">
      <div class="product-shot" role="img" aria-label="Gold pump lotion bottle" style="background:linear-gradient(180deg,#f7f3ef,#e2c173 40%,#c79b3e)"></div>
      <h3>Vestibulum Purus</h3><p>Condimentum ultricies ut ipsum Quam auctor euismod</p><div class="price">$142.00</div><a class="btn-outline">ADD TO CART</a>
    </div>
    <div class="product">
      <div class="product-shot" role="img" aria-label="Cream tubes and jar" style="background:linear-gradient(180deg,#f7f3ef,#f0e6dc 40%,#e59a6b)"></div>
      <h3>Vestibulum Purus</h3><p>Condimentum ultricies ut ipsum Quam auctor euismod</p><div class="price">$142.00</div><a class="btn-outline">ADD TO CART</a>
    </div>
    <div class="product">
      <div class="product-shot" role="img" aria-label="Pink cosmetic jars and bottles" style="background:linear-gradient(180deg,#f7f3ef,#f2c8d4 50%,#e39fb4)"></div>
      <h3>Vestibulum Purus</h3><p>Condimentum ultricies ut ipsum Quam auctor euismod</p><div class="price">$142.00</div><a class="btn-outline">ADD TO CART</a>
    </div>
  </div>
</section>

<div class="rule" style="top:1380px"></div>

<h2 class="blog-title">FROM THE BLOG</h2>
<div class="blog-title-rule"></div>
<article class="post" style="left:172px">
  <div class="post-photo" role="img" aria-label="Woman with long blonde hair" style="background:linear-gradient(135deg,#3a2a1e,#b88a55 50%,#d9b985)"></div>
  <div class="post-panel"><h3>Proin fermentum &amp;<br>Augue quis tincidunt aliquet</h3><p>Sit amet semper ipsum risus nec felis</p></div>
  <a class="btn-outline">READ MORE</a>
</article>
<article class="post" style="left:612px">
  <div class="post-photo" role="img" aria-label="Woman relaxing on a white floor" style="background:linear-gradient(135deg,#f2efec,#e3dcd5 50%,#b58a5e)"></div>
  <div class="post-panel"><h3>Proin fermentum &amp;<br>Augue quis tincidunt aliquet</h3><p>Sit amet semper ipsum risus nec felis</p></div>
  <a class="btn-outline">READ MORE</a>
</article>

<section class="consult">
  <h2>Dermatologist Consultation</h2>
  <p class="copy">Praesent urna mauris, faucibus vel semper sed, imperdiet varius nisi. Proin ac porttitor eros. Donec rhoncus vitae nunc sed elementum. Quisque facilisis volutpat.</p>
  <div class="doctor" role="img" aria-label="Portrait of the consulting dermatologist"></div>
  <p class="quote">Proin fermentum, a augue quis tincidunt aliquet</p>
  <div class="consult-nav"><span>‹</span><span>›</span></div>
</section>

<section class="signup">
  <h4 style="left:172px">Sign up for email</h4>
  <div class="signup-form"><span class="field">Enter your email address</span><span class="submit">SIGN UP</span></div>
  <h4 style="left:760px">Stay Connected</h4>
  <div class="social"><span></span><span></span><span></span><span></span></div>
</section>

<footer class="site-footer">
  <div class="footer-col" style="left:172px"><h5>Philosophy</h5><ul><li>Praesent urna mauris</li><li>Faucibus vel semper sed</li><li>Imperdiet varius nisi Proin ac porttitor</li><li>Donec rhoncus vitae nunc sed</li><li>Elementum, Quisque facilisis</li><li>Volutpat erat et mattis</li></ul></div>
  <div class="footer-col" style="left:468px"><h5>Our Doctors</h5><ul><li>Doctor Formulated</li><li>Dermatologist Team</li><li>Freshly Handmade</li><li>Registered Pharmacy</li><li>Skin Condition Advice</li><li>Active Ingredients</li><li>Journal Resources</li></ul></div>
  <div class="footer-col" style="left:760px"><h5>Customer Care</h5><ul><li>Contact Us</li><li>Shipping Information</li><li>Return and Exchange</li><li>Auto delivery services</li><li>Complimentary services</li><li>FAQs</li></ul></div>
  <p class="copyright">© 2024 Orvan Kesto. All rights reserved.</p>
</footer>

</body>
</html>
```